Step Up Personal Training Sessions

Whether you have a lot to give out or a little...just Step Up. Whether you are strong or you desire to get there... just Step Up. Stay Bold Feel Free. PT's with a passionate coach.

I had imagined black and white or indigo/white. Communicate love, people and fitness.

Target Market(s)

Women, men, disabilities. People whom wish to move more, or who do not desire to go to a gym. One on one fitness or small group training.

Industry/Entity Type

Training

Contact Information for Business Card

Kim Harlow
0431 552 907
kimjoanne@fastmailbox.com

Font styles to use
Decorative

Colors
0d0d0d
1b1b1b

Requirements
Must have
• Step Up
• Personal Fitness Sessions
• Stay Bold Feel Free
• ( my details above )
Nice to have
• If any part of the project description ....Whether....etc
• can be fit onto card. That would be great. I had ideas of Heart, people exercising, I love boxing training, so this idea was in my head, not sure how to bring all together. Would also like to work with disabilities.
Should not have
• Cannot think of any not haves at this stage.
• Colours at the bottom of page, either green is ok, with charcoal or navy. Not both these colours together.

```html
<!DOCTYPE html>
<html lang="en">
<head>
<meta charset="utf-8">
<title>Step Up Personal Fitness Sessions</title>
<link rel="stylesheet" href="https://fonts.googleapis.com/css2?family=Amatic+SC:wght@700&family=Cormorant+SC:wght@500&family=Rye&family=Fredericka+the+Great&display=swap">
<style>
  :root {
    --ink: #0d0d0d;
    --charcoal: #1b1b1b;
    --panel: #2e2e2e;
    --green-deep: #0f9a45;
    --green-mid: #3cb64a;
    --green-light: #8cc63f;
    --green-haze: #7fa877;
    --photo-light: #6c7375;
    --photo-dark: #3f4547;
    --white: #ffffff;
  }
  html, body {
    margin: 0;
    padding: 0;
    overflow: hidden;
    background: var(--ink);
  }
  .card {
    position: relative;
    width: 1200px;
    height: 720px;
    overflow: hidden;
    background: linear-gradient(180deg, var(--green-haze) 0%, #4b6b48 16%, #222 36%, var(--ink) 60%, var(--charcoal) 100%);
  }
  .card__shapes {
    position: absolute;
    inset: 0;
  }
  .headline {
    position: absolute;
    margin: 0;
    font-family: "Amatic SC", cursive;
    font-weight: 700;
    color: var(--white);
    line-height: 1;
    font-size: 76px;
    letter-spacing: 1px;
    text-shadow: 1px 2px 3px rgba(0,0,0,.4);
    white-space: nowrap;
  }
  .headline--service { left: 16px; top: 4px; }
  .headline--motto { left: 72px; top: 92px; }
  .headline--brand { left: 232px; top: 180px; }
  .mission {
    position: absolute;
    left: 894px;
    top: 240px;
    margin: 0;
    font-family: "Cormorant SC", serif;
    font-weight: 500;
    font-size: 20.5px;
    line-height: 31px;
    color: var(--white);
    white-space: nowrap;
  }
  .mission span { display: block; }
  .mission .indent { padding-left: 20px; }
  .mission .nudge { padding-left: 6px; }
  .contact__name {
    position: absolute;
    left: 20px;
    top: 638px;
    margin: 0;
    font-family: "Rye", serif;
    font-size: 38px;
    color: var(--white);
    letter-spacing: 2px;
    white-space: nowrap;
  }
  .contact__email {
    position: absolute;
    left: 4px;
    top: 684px;
    margin: 0;
    font-family: "Fredericka the Great", serif;
    font-size: 26px;
    color: var(--white);
    letter-spacing: 1px;
    white-space: nowrap;
  }
  .contact__phone {
    position: absolute;
    right: 30px;
    top: 664px;
    margin: 0;
    font-family: "Rye", serif;
    font-size: 40px;
    color: var(--ink);
    letter-spacing: 5px;
    white-space: nowrap;
  }
</style>
</head>
<body>
<main class="card">
  <svg class="card__shapes" width="1200" height="720" viewBox="0 0 1200 720">
    <defs>
      <radialGradient id="photo-fill" cx="45%" cy="40%" r="65%">
        <stop offset="0%" stop-color="var(--photo-light)"/>
        <stop offset="100%" stop-color="var(--photo-dark)"/>
      </radialGradient>
    </defs>
    <path d="M0 408 C180 400 360 440 520 500 C680 560 820 570 960 520 C1060 480 1140 430 1200 410 L1200 720 L0 720 Z" fill="var(--green-light)"/>
    <path d="M0 470 C200 470 380 510 520 560 C660 610 820 610 960 560 C1060 520 1140 480 1200 460 L1200 720 L0 720 Z" fill="var(--green-deep)"/>
    <path d="M0 500 C200 500 380 540 520 600 C640 650 820 620 960 580 C1060 550 1140 520 1200 505 L1200 720 L0 720 Z" fill="var(--charcoal)"/>
    <path d="M0 530 C200 540 360 570 520 640 C620 680 700 690 760 700 L0 720 Z" fill="var(--green-mid)" opacity=".9"/>
    <path d="M0 560 C220 570 400 610 560 690 L0 720 Z" fill="var(--charcoal)"/>
    <path d="M560 510 C700 560 860 580 1010 540 C1100 515 1160 480 1200 460 L1200 490 C1130 530 1040 570 920 585 C800 600 680 580 560 530 Z" fill="var(--green-mid)"/>
    <circle cx="654" cy="301" r="228" fill="none" stroke="var(--green-mid)" stroke-width="20"/>
    <circle cx="654" cy="301" r="212" fill="none" stroke="var(--green-deep)" stroke-width="8"/>
    <circle class="photo" cx="654" cy="301" r="202" fill="url(#photo-fill)" role="img" aria-label="Photograph of a boxer in red gloves punching a heavy bag"/>
    <path d="M448 656 L1200 656 L1200 720 L448 720 Z" fill="var(--green-light)"/>
    <path d="M0 644 L430 644 L500 720 L0 720 Z" fill="var(--panel)"/>
  </svg>

  <h1 class="headline headline--service">Personal Fitness Sessions</h1>
  <p class="headline headline--motto">Stay Bold Feel Free</p>
  <p class="headline headline--brand">Step Up</p>

  <p class="mission">
    <span class="nudge">Fitness is to empower</span>
    <span class="indent">you to become</span>
    <span class="nudge">the strongest, healthiest,</span>
    <span>most confident and unstoppable</span>
  </p>

  <p class="contact__name">Kim Harlow</p>
  <p class="contact__email">KIMJOANNE@FASTMAILBOX.COM</p>
  <p class="contact__phone">CALL US: 0431 552 907</p>
</main>
</body>
</html>
```